CD Cover Design Project - Marisol Fenwick

We need an ablum / cd cover design for the artist Marisol Fenwick - www.marisolfenwick.com

The album is called "Quiet Rooms Of Paper"

General
A ‘Quiet Rooms’ is a very traditional and formal art form. With this in mind, the artwork should have an ‘old’ feel, for lack of a better word. I don’t envision anything too contemporary or clean., I imagine something like an old letter or photograph, yellow round the edges and somehow nostalgic.

Colour scheme
This should not be too saturated with colour, but not devoid of it either. I’m a fan of colour – it definitely needs to be in there! We just need to base it on the main image, derive the colour palette from there and reference it constantly.

Font
In keeping with the idea of an old letter, this should be something like an old feather quill and ink, if possible. Can this be hand-written???

Reverse of CD:

Track Listing

MERIDOSA
Fenwick, Ashcombe

LATCH
Fenwick

BLUE DUNES
Fenwick

IF WE BEND
Fenwick, Ashcombe

PAPER LANTERN
Fenwick, Ashcombe

RESTLESS TIDE
Fenwick, Pritch

MENDING A NET
Dorsey/Halloran

ALONG THE OLD PATH
Fenwick

COAT IN WINTER
Fenwick, Tamsett

VELMO
Fenwick, Fenwick

Quiet Rooms produced by Marisol Fenwick, Tom Vellacott, Rob Pell & Jake Orsted

All tracks except Velmo recorded first at Tinwhistle Rooms London with Stephen Calloway, then engineered and produced by Tom Vellacott at Brenvik, then final production and finishing touches at Lanternfish Studios with Rob Pell & Jake Orsted. Velmo was recorded at xxxx with Howard Stellmach and finished at Lanternfish Studios with Rob Pell & Jake Orsted.

Barcode (dummy please)

Management TurnTheKey ltd - admin@turnthekey.ltd.uk 0207 946 0321

©TurnTheKey Publishing 2013. All rights reserverd. Unauthorised
copying, reproduction, hiring, public performance and broadcasting prohibited. www.turnthekey.ltd.uk

Industry/Entity Type

Management

Requirements
Must have
• You need to use this image on the cover:

https://www.filedrawer-example.net/s/k7pq2wz9rtxmv31/Marisol-QuietRooms_Cover.tif

I have uploaded the jpg but this is better quality.

```html
<!DOCTYPE html>
<html lang="en">
<head>
<meta charset="utf-8">
<title>Quiet Rooms Of Paper – Back Cover</title>
<link href="https://fonts.googleapis.com/css2?family=Bebas+Neue&display=swap" rel="stylesheet">
<style>
  :root {
    --page: #ffffff;
    --ink: #f4d7f0;
    --shade-deep: #1f140c;
    --shade-mid: #3b2615;
    --shade-warm: #5a3a1f;
    --leaf: #2c3a22;
    --petal: #7a5a5e;
    --label: #ffffff;
  }
  * { margin: 0; padding: 0; box-sizing: border-box; }
  html, body {
    width: 1200px; height: 1000px; overflow: hidden;
    background: var(--page);
  }
  .back-cover {
    position: absolute; left: 94px; top: 0;
    width: 1004px; height: 1000px;
    overflow: hidden;
    font-family: "Bebas Neue", "Oswald", sans-serif;
    color: var(--ink);
  }
  .still-life-art {
    position: absolute; inset: 0;
    background:
      radial-gradient(ellipse 420px 200px at 420px 90px, rgba(122,90,94,0.55), transparent 70%),
      radial-gradient(ellipse 300px 260px at 560px 340px, rgba(44,58,34,0.7), transparent 70%),
      radial-gradient(ellipse 260px 200px at 880px 760px, rgba(150,120,80,0.45), transparent 70%),
      radial-gradient(ellipse 300px 160px at 860px 320px, rgba(110,78,40,0.45), transparent 70%),
      linear-gradient(160deg, var(--shade-mid) 0%, var(--shade-deep) 45%, var(--shade-warm) 100%);
  }
  .tracks { position: absolute; left: 16px; top: 8px; }
  .tracks-heading { font-size: 29px; line-height: 32px; font-weight: 400; letter-spacing: 0.3px; }
  .track-list { list-style: none; margin-top: 39px; }
  .track { height: 86px; }
  .track-title { display: block; font-size: 24px; line-height: 26px; letter-spacing: 0.3px; }
  .track-writers { display: block; font-size: 18px; line-height: 20px; letter-spacing: 0.3px; }
  .credits {
    position: absolute; right: 15px; top: 12px; width: 580px;
    text-align: right; font-size: 18px; line-height: 23.8px; letter-spacing: 0.3px;
  }
  .credits p + p { margin-top: 24px; }
  .code-label {
    position: absolute; left: 355px; top: 783px;
    width: 321px; height: 154px; background: var(--label);
  }
  .legal {
    position: absolute; left: 0; right: 0; top: 955px;
    text-align: center; font-size: 18px; line-height: 23px; letter-spacing: 0.3px;
  }
</style>
</head>
<body>
  <div class="back-cover">
    <div class="still-life-art" role="img" aria-label="Dim still life photograph: pink lilies and green leaves in a glass vase, an ornate gilt frame, wooden percussion, seed shakers and a tambourine on a dark table"></div>

    <section class="tracks">
      <h2 class="tracks-heading">TRACKS</h2>
      <ol class="track-list">
        <li class="track"><span class="track-title">MERIDOSA</span><span class="track-writers">FENWICK, ASHCOMBE</span></li>
        <li class="track"><span class="track-title">LATCH</span><span class="track-writers">FENWICK</span></li>
        <li class="track"><span class="track-title">BLUE DUNES</span><span class="track-writers">FENWICK</span></li>
        <li class="track"><span class="track-title">IF WE BEND</span><span class="track-writers">FENWICK, ASHCOMBE</span></li>
        <li class="track"><span class="track-title">PAPER LANTERN</span><span class="track-writers">FENWICK, ASHCOMBE</span></li>
        <li class="track"><span class="track-title">RESTLESS TIDE</span><span class="track-writers">FENWICK, PRITCH</span></li>
        <li class="track"><span class="track-title">MENDING A NET</span><span class="track-writers">DORSEY/HALLORAN</span></li>
        <li class="track"><span class="track-title">ALONG THE OLD PATH</span><span class="track-writers">FENWICK</span></li>
        <li class="track"><span class="track-title">COAT IN WINTER</span><span class="track-writers">FENWICK, TAMSETT</span></li>
        <li class="track"><span class="track-title">VELMO</span><span class="track-writers">FENWICK, FENWICK</span></li>
      </ol>
    </section>

    <section class="credits">
      <p>QUIET ROOMS PRODUCED BY MARISOL FENWICK, TOM VELLACOTT, ROB PELL &amp; JAKE ORSTED</p>
      <p>ALL TRACKS EXCEPT VELMO RECORDED FIRST AT TINWHISTLE ROOMS LONDON WITH STEPHEN CALLOWAY, THEN ENGINEERED AND PRODUCED BY TOM VELLACOTT AT BRENVIK, THEN FINAL PRODUCTION AND FINISHING TOUCHES AT LANTERNFISH STUDIOS WITH ROB PELL &amp; JAKE ORSTED. VELMO WAS RECORDED AT XXXX WITH HOWARD STELLMACH AND FINISHED AT LANTERNFISH STUDIOS WITH ROB PELL &amp; JAKE ORSTED.</p>
      <p>MANAGEMENT TURNTHEKEY LTD - ADMIN@TURNTHEKEY.LTD.UK 0207 946 0321</p>
    </section>

    <div class="code-label"></div>

    <footer class="legal">
      <p>©TURNTHEKEY PUBLISHING 2013. ALL RIGHTS RESERVERD.</p>
      <p>UNAUTHORISED COPYING, REPRODUCTION, HIRING, PUBLIC PERFORMANCE AND BROADCASTING PROHIBITED. WWW.TURNTHEKEY.LTD.UK</p>
    </footer>
  </div>
</body>
</html>
```